Tidal Homecare

I am looking to have a website designed for a housekeeping company that looks similar to this one. https://marlowestidyhomes.example/

I need 5 websites designed but will start with this one to see how I like it.

Industry/Entity Type

House Cleaning

Coding

Coded - Design and coding required

Number of Pages Required

5+ page

Font styles to use
Serif
Script

Colors
ffffff
fdf9cf
fbf289
fbee3f
d6edf3
86cae7
33a6d7
edf1f8
cedeed

```html
<!DOCTYPE html>
<html lang="en">
<head>
<meta charset="utf-8">
<title>Tidal Homecare</title>
<link href="https://fonts.googleapis.com/css2?family=Roboto:wght@400;500;700&family=Lato:wght@400;700&display=swap" rel="stylesheet">
<style>
:root{
  --blue:#33a6d7;
  --blue-dark:#2a8fc4;
  --ink:#1e1e1e;
  --text:#333;
  --muted:#8a8a8a;
  --panel:#d6edf3;
  --card:#edf1f8;
  --rule:#9a9a9a;
  --footer:#1a1a1a;
  --white:#ffffff;
}
*{margin:0;padding:0;box-sizing:border-box}
html,body{width:1200px;height:3057px;overflow:hidden;background:var(--white)}
body{position:relative;font-family:"Lato",sans-serif;color:var(--text)}
.abs{position:absolute}
.btn{position:absolute;background:var(--blue);color:var(--white);font-family:"Roboto",sans-serif;text-align:center;text-transform:uppercase;letter-spacing:.3px}
.rule{position:absolute;height:3px;background:var(--rule)}
.section-title{position:absolute;left:0;width:1200px;text-align:center;font-family:"Roboto",sans-serif;font-weight:700;font-size:26px;color:var(--ink)}

/* header */
.header{position:absolute;left:0;top:0;width:1200px;height:103px;background:var(--white)}
.brand{position:absolute;left:133px;top:22px;display:flex;align-items:center;gap:14px}
.brand-mark{width:46px;height:46px;border-radius:50%;background:var(--blue)}
.brand-name{font-family:"Roboto",sans-serif;font-weight:700;font-size:24px;line-height:26px;color:var(--blue)}
.call{position:absolute;left:760px;top:20px;display:flex;gap:8px;align-items:center}
.call small{display:block;font-family:"Roboto",sans-serif;font-size:10px;color:var(--ink)}
.call strong{display:block;font-family:"Roboto",sans-serif;font-weight:500;font-size:18px;color:var(--ink)}
.nav{position:absolute;right:132px;top:70px;display:flex;gap:29px;font-family:"Roboto",sans-serif;font-weight:500;font-size:15px;color:var(--ink)}

/* hero */
.hero-photo{position:absolute;left:0;top:103px;width:1200px;height:577px;background:linear-gradient(180deg,#e8e6e1 0%,#cfc8bd 45%,#8e7460 75%,#5a3e2c 100%)}
.hero-box{position:absolute;left:376px;top:262px;width:448px;height:202px;background:rgba(255,255,255,.9);text-align:center}
.hero-box h1{margin-top:26px;font-family:"Roboto",sans-serif;font-weight:700;font-size:35px;color:var(--ink)}
.hero-box p{margin-top:10px;font-family:"Roboto",sans-serif;font-size:17px;line-height:22px;color:var(--ink)}

/* services */
.service{position:absolute;top:840px;width:270px;text-align:center}
.service svg{display:block;margin:0 auto}
.service h3{margin-top:40px;font-family:"Roboto",sans-serif;font-weight:500;font-size:20px;color:var(--ink)}
.service p{margin-top:16px;font-size:14px;line-height:18.5px;color:var(--text)}
.service .btn{position:static;display:inline-block;margin-top:25px;width:93px;height:28px;line-height:28px;font-size:12px}

/* welcome */
.welcome-photo{position:absolute;left:0;top:1198px;width:598px;height:458px;background:linear-gradient(135deg,#d9e2ea 0%,#b9c8d6 40%,#e4c53a 65%,#3a3a3a 100%)}
.welcome-panel{position:absolute;left:598px;top:1198px;width:602px;height:458px;background:var(--panel)}
.welcome-panel h2{position:absolute;left:64px;top:52px;font-family:"Roboto",sans-serif;font-size:24px;line-height:34px;font-weight:500;color:var(--ink)}
.welcome-panel h2 b{font-weight:700;font-size:26px}
.welcome-panel p{position:absolute;left:65px;top:173px;width:380px;font-size:14.5px;line-height:19.3px;color:var(--ink)}

/* testimonials */
.quote-card{position:absolute;top:1814px;width:294px;height:340px;background:var(--card)}
.quote-card .mark{position:absolute;font-family:"Roboto",sans-serif;font-weight:700;font-size:40px;color:#a8adb5;line-height:1}
.quote-card p{position:absolute;left:50px;top:54px;width:210px;font-size:14.5px;line-height:19.3px;color:#444}
.quote-card .who{position:absolute;left:50px;top:272px;display:flex;gap:10px;align-items:center}
.avatar{width:30px;height:30px;border-radius:50%;background:#8e9aa8}
.who strong{display:block;font-family:"Roboto",sans-serif;font-weight:500;font-size:13px;color:var(--ink)}
.who span{display:block;font-size:11px;color:#555}
.arrow{position:absolute;top:1968px;width:32px;height:32px;border-radius:50%;background:var(--blue)}

/* estimate */
.estimate-photo{position:absolute;left:0;top:2228px;width:1200px;height:435px;background:linear-gradient(90deg,#f4f3f1 0%,#f1efec 38%,#c9c2b6 62%,#8aa0b4 80%,#b08a5a 100%)}
.estimate-fade{position:absolute;left:0;top:2228px;width:620px;height:435px;background:rgba(255,255,255,.75)}
.estimate h2{position:absolute;left:131px;top:2276px;font-family:"Roboto",sans-serif;font-weight:700;font-size:25px;color:var(--ink)}
.field{position:absolute;width:200px;height:36px;border:2px solid #777;background:rgba(255,255,255,.6);font-family:"Roboto",sans-serif;font-size:12px;color:var(--ink);padding:0 12px;line-height:32px}
.field svg{position:absolute;right:10px;top:11px}

/* footer */
.footer{position:absolute;left:0;top:2663px;width:1200px;height:394px;background:var(--footer);color:#e6e6e6}
.footer h4{position:absolute;font-family:"Roboto",sans-serif;font-weight:700;font-size:15px;color:var(--white)}
.footer-menu{position:absolute;left:507px;top:102px;list-style:none;font-size:13.5px;line-height:22.5px;font-family:"Roboto",sans-serif}
.contact-row{position:absolute;display:flex;gap:12px;align-items:flex-start;font-family:"Roboto",sans-serif;font-size:13.5px;line-height:18px}
.dot{flex:none;width:26px;height:26px;border-radius:50%;background:var(--blue);margin-top:4px}
.footer-line{position:absolute;left:140px;top:300px;width:920px;height:1px;background:#333}
.copyright{position:absolute;left:0;top:348px;width:1200px;text-align:center;font-size:11px;color:#ddd}
</style>
</head>
<body>

<header class="header">
  <div class="brand">
    <span class="brand-mark"></span>
    <span class="brand-name">Tidal<br>Homecare</span>
  </div>
  <div class="call">
    <svg width="26" height="26" viewBox="0 0 24 24" fill="none" stroke="#1e1e1e" stroke-width="1.6"><path d="M5 3h4l2 5-2.5 1.5a11 11 0 0 0 6 6L16 13l5 2v4a2 2 0 0 1-2 2A17 17 0 0 1 3 5a2 2 0 0 1 2-2z"/></svg>
    <div><small>CALL US</small><strong>555.014.2260</strong></div>
  </div>
  <a class="btn" style="left:931px;top:18px;width:137px;height:35px;line-height:35px;font-size:15px">Free Estimate</a>
  <nav class="nav"><span>HOME</span><span>ABOUT US</span><span>SERVICES</span><span>GIFT CARDS</span><span>CONTACT</span></nav>
</header>

<section>
  <div class="hero-photo" role="img" aria-label="Bright modern kitchen with white cabinets, pendant lights and a marble island"></div>
  <div class="hero-box">
    <h1>HOUSEKEEPING</h1>
    <p>LOREM IPSUM IS SIMPLY DUMMY TEXT OF THE<br>PRINTING AND TYPESETTING INDUSTRY.</p>
    <a class="btn" style="left:156px;top:143px;width:137px;height:34px;line-height:34px;font-size:15px">Free Estimate</a>
  </div>
</section>

<section>
  <h2 class="section-title" style="top:733px">OUR SERVICES</h2>
  <div class="rule" style="left:574px;top:776px;width:52px"></div>

  <div class="service" style="left:128px">
    <svg width="94" height="94" viewBox="0 0 94 94" fill="none" stroke="#33a6d7" stroke-width="2.5">
      <path d="M22 4h50M32 4v8M47 4v8M62 4v8"/><path d="M27 12h10l-2 7h-6zM42 12h10l-2 7h-6zM57 12h10l-2 7h-6z"/>
      <rect x="16" y="44" width="62" height="24" rx="4"/><path d="M20 44v-10a6 6 0 0 1 6-6h42a6 6 0 0 1 6 6v10"/>
      <rect x="6" y="48" width="12" height="26" rx="5"/><rect x="76" y="48" width="12" height="26" rx="5"/>
      <path d="M12 74h70M16 74v6M78 74v6"/>
    </svg>
    <h3>Residential Cleaning</h3>
    <p>Lorem ipsum dolor sit amet, consectetur adipiscing elit, sed do eiusmod tempor incididunt ut labore et dolore magna aliqua. Ut enim ad minim</p>
    <a class="btn">Read More</a>
  </div>

  <div class="service" style="left:465px">
    <svg width="94" height="94" viewBox="0 0 94 94" fill="none" stroke="#33a6d7" stroke-width="2.5">
      <rect x="22" y="4" width="50" height="86"/><rect x="10" y="30" width="12" height="60"/><rect x="72" y="30" width="12" height="60"/>
      <path d="M30 12h8v8h-8zM43 12h8v8h-8zM56 12h8v8h-8zM30 26h8v8h-8zM43 26h8v8h-8zM56 26h8v8h-8zM30 40h8v8h-8zM43 40h8v8h-8zM56 40h8v8h-8zM30 54h8v8h-8zM43 54h8v8h-8zM56 54h8v8h-8z"/>
      <path d="M38 90V72h18v18"/>
    </svg>
    <h3>Commercial Cleaning</h3>
    <p>Lorem ipsum dolor sit amet, consectetur adipiscing elit, sed do eiusmod tempor incididunt ut labore et dolore magna aliqua. Ut enim ad minim</p>
    <a class="btn">Read More</a>
  </div>

  <div class="service" style="left:801px">
    <svg width="94" height="94" viewBox="0 0 94 94" fill="none" stroke="#33a6d7" stroke-width="2.5">
      <rect x="10" y="4" width="74" height="54" rx="3"/><path d="M10 46h74M40 58l-3 12M54 58l3 12"/>
      <rect x="14" y="70" width="58" height="16" rx="2"/><path d="M20 76h46M20 81h46"/><circle cx="82" cy="78" r="6"/>
    </svg>
    <h3>Additional Cleaning</h3>
    <p>Lorem ipsum dolor sit amet, consectetur adipiscing elit, sed do eiusmod tempor incididunt ut labore et dolore magna aliqua. Ut enim ad minim</p>
    <a class="btn">Read More</a>
  </div>
</section>

<section>
  <div class="welcome-photo" role="img" aria-label="Hand in a yellow rubber glove wiping a dark countertop with a cloth"></div>
  <div class="welcome-panel">
    <h2>Welcome to<br><b>TIDAL HOMECARE</b></h2>
    <div class="rule" style="left:64px;top:133px;width:52px"></div>
    <p>At vero eos et accusamus et iusto odio dignissimos ducimus qui blanditiis praesentium voluptatum deleniti atque corrupti quos dolores et quas molestias excepturi sint occaecati cupiditate non provident, similique sunt in culpa qui officia deserunt mollitia animi, id est laborum et dolorum fuga. Et harum quidem rerum facilis est et expedita distinctio. Nam libero tempore, cum soluta nobis est eligendi optio cumque nihil impedit quo minus.</p>
    <a class="btn" style="left:68px;top:366px;width:111px;height:34px;line-height:34px;font-size:15px">Read More</a>
  </div>
</section>

<section>
  <h2 class="section-title" style="top:1715px">TESTIMONIALS</h2>
  <div class="rule" style="left:574px;top:1760px;width:52px"></div>

  <div class="arrow" style="left:64px"><svg width="32" height="32" viewBox="0 0 32 32" fill="none" stroke="#fff" stroke-width="2"><path d="M18 11l-5 5 5 5"/></svg></div>
  <div class="arrow" style="left:1100px"><svg width="32" height="32" viewBox="0 0 32 32" fill="none" stroke="#fff" stroke-width="2"><path d="M14 11l5 5-5 5"/></svg></div>

  <div class="quote-card" style="left:132px">
    <span class="mark" style="left:26px;top:28px">&ldquo;</span>
    <p>Lorem Ipsum is simply dummy text of the printing and types etting industry. Lorem Ipsum has been the industry's stan dard dummy text ever since the 1500s, when an unknown prin ter took a galley of type and scram bled it to make a type specimen book. It has survived not only .</p>
    <span class="mark" style="left:176px;top:238px">&rdquo;</span>
    <div class="who"><span class="avatar"></span><div><strong>MARTIN</strong><span>Cornwall</span></div></div>
  </div>
  <div class="quote-card" style="left:452px">
    <span class="mark" style="left:26px;top:28px">&ldquo;</span>
    <p>Lorem Ipsum is simply dummy text of the printing and types etting industry. Lorem Ipsum has been the industry's stan dard dummy text ever since the 1500s, when an unknown prin ter took a galley of type and scram bled it to make a type specimen book. It has survived not only .</p>
    <span class="mark" style="left:176px;top:238px">&rdquo;</span>
    <div class="who"><span class="avatar"></span><div><strong>MARTIN</strong><span>Cornwall</span></div></div>
  </div>
  <div class="quote-card" style="left:772px">
    <span class="mark" style="left:26px;top:28px">&ldquo;</span>
    <p>Lorem Ipsum is simply dummy text of the printing and types etting industry. Lorem Ipsum has been the industry's stan dard dummy text ever since the 1500s, when an unknown prin ter took a galley of type and scram bled it to make a type specimen book. It has survived not only .</p>
    <span class="mark" style="left:176px;top:238px">&rdquo;</span>
    <div class="who"><span class="avatar"></span><div><strong>MARTIN</strong><span>Cornwall</span></div></div>
  </div>
</section>

<section class="estimate">
  <div class="estimate-photo" role="img" aria-label="Airy dining room with wooden table, dark chairs and a living area beyond"></div>
  <div class="estimate-fade"></div>
  <h2>FREE ESTIMATE</h2>
  <div class="rule" style="left:133px;top:2314px;width:50px"></div>
  <div class="field" style="left:133px;top:2352px">NAME</div>
  <div class="field" style="left:345px;top:2352px">E MAIL</div>
  <div class="field" style="left:133px;top:2402px">CITY</div>
  <div class="field" style="left:345px;top:2402px">SQUAR FOOTAGE</div>
  <div class="field" style="left:133px;top:2455px">PROPERTY TYPE<svg width="10" height="10" viewBox="0 0 10 10"><path d="M1 3h8L5 8z" fill="#333"/></svg></div>
  <div class="field" style="left:345px;top:2455px">TYPE OF CLEANING<svg width="10" height="10" viewBox="0 0 10 10"><path d="M1 3h8L5 8z" fill="#333"/></svg></div>
  <div class="field" style="left:133px;top:2507px">FREQUENCY<svg width="10" height="10" viewBox="0 0 10 10"><path d="M1 3h8L5 8z" fill="#333"/></svg></div>
  <div class="field" style="left:345px;top:2507px">DD/MM/YYYY<svg width="12" height="12" viewBox="0 0 12 12" fill="none" stroke="#333"><rect x="1" y="2" width="10" height="9"/><path d="M1 5h10M4 1v2M8 1v2"/></svg></div>
  <a class="btn" style="left:133px;top:2568px;width:98px;height:38px;line-height:38px;font-size:15px;font-weight:700">Submit</a>
</section>

<footer class="footer">
  <div class="brand" style="left:132px;top:70px">
    <span class="brand-mark"></span>
    <span class="brand-name">Tidal<br>Homecare</span>
  </div>

  <h4 style="left:507px;top:60px">MENU</h4>
  <ul class="footer-menu"><li>HOME</li><li>ABOUT US</li><li>SERVICES</li><li>GIFT CARDS</li><li>CONTACT</li></ul>

  <h4 style="left:662px;top:60px">CONTACT US</h4>
  <div class="contact-row" style="left:660px;top:102px"><span class="dot"></span><span>2217 Shoreline Lane<br>Bayview, CA 90000</span></div>
  <div class="contact-row" style="left:660px;top:160px"><span class="dot"></span><span>Call Us<br>555.014.2260</span></div>
  <div class="contact-row" style="left:660px;top:218px"><span class="dot"></span><span>E mail Us<br>hello@tidalhomecare.example</span></div>

  <h4 style="left:952px;top:60px">FOLLOW US</h4>
  <div class="contact-row" style="left:950px;top:102px"><span class="dot"></span><span>Like us on<br>SOCIALHUB</span></div>
  <div class="contact-row" style="left:950px;top:160px"><span class="dot"></span><span>Follow us on<br>CHIRPLINE</span></div>
  <div class="contact-row" style="left:950px;top:218px"><span class="dot"></span><span>Follow us on<br>WORKNET</span></div>

  <div class="footer-line"></div>
  <p class="copyright">Copyright © 2020 All Rights Reserved</p>
</footer>

</body>
</html>
```